Asia Hotel need a card and logo

The new hotel in East Asia, Taiwan need a business card and logo design.The hotel's Chinese name is 岚柏文旅,English name is "Velmira Hotel".The core concept of this hotel is "Eco green", going to use many plant etc.,The building's first outlook draft is attached in the file for your reference.The style be modern and fashion will be good. Thank you.
Target Market(s)
East Asia
Industry/Entity Type
Hotel
Contact Information for Business Card
The hotel's name both in Chinese and English :岚柏商旅 Velmira Hotel
The logo, address, E-mail and tel number place.
Stuff's name and title.
Font styles to use
Colors
Designer to choose colors to be used in the design.
Look and feel
Each slider illustrates characteristics of the customer's brand and the style your logo design should communicate.

```html
<!DOCTYPE html>
<html lang="en">
<head>
<meta charset="utf-8">
<title>Velmira Hotel – Business Card</title>
<link rel="stylesheet" href="https://fonts.googleapis.com/css2?family=Pathway+Gothic+One&family=Quicksand:wght@400;700&family=Didact+Gothic&family=Noto+Sans+TC:wght@400&display=swap">
<style>
  :root {
    --backdrop: #4d8865;
    --card-light: #ffffff;
    --card-shade: #e9e9eb;
    --brand-green: #1f7a1f;
    --deep-green: #0f4d14;
    --leaf-green: #3aa032;
    --ink-blue: #34517f;
  }
  * { margin: 0; padding: 0; box-sizing: border-box; }
  html, body { width: 900px; height: 1200px; overflow: hidden; }
  body { background: var(--backdrop); position: relative; font-family: "Didact Gothic", sans-serif; }

  .card {
    position: absolute;
    left: 57px;
    width: 804px;
    height: 460px;
    background: linear-gradient(115deg, var(--card-light) 30%, var(--card-shade) 100%);
    box-shadow: 6px 10px 18px rgba(0, 0, 0, 0.22);
    overflow: hidden;
  }
  .card-front { top: 92px; }
  .card-back { top: 656px; }

  .emblem-area {
    position: absolute;
    left: 282px; top: 28px;
    width: 240px; height: 240px;
    border-radius: 50%;
    background: radial-gradient(circle at 45% 40%, #4fae3f 0%, var(--leaf-green) 55%, #2a7d26 100%);
  }
  .brand-name {
    position: absolute;
    left: 0; right: 0; top: 290px;
    text-align: center;
    font-family: "Pathway Gothic One", sans-serif;
    font-weight: 400;
    font-size: 62px;
    letter-spacing: 1px;
    color: var(--brand-green);
    line-height: 1;
  }
  .brand-name-zh {
    position: absolute;
    left: 0; right: 0; top: 370px;
    text-align: center;
    font-family: "Noto Sans TC", sans-serif;
    font-weight: 400;
    font-size: 24px;
    letter-spacing: 10px;
    padding-left: 10px;
    color: var(--brand-green);
    line-height: 1;
  }

  .frame-lines { position: absolute; inset: 0; width: 100%; height: 100%; }
  .frame-lines path { fill: none; stroke: var(--ink-blue); stroke-width: 2; }

  .holder {
    position: absolute;
    left: 0; right: 0; top: 58px;
    text-align: center;
    padding-left: 28px;
    font-family: "Quicksand", sans-serif;
    line-height: 1;
  }
  .holder-name { font-weight: 700; }
  .holder-first { font-size: 60px; color: var(--brand-green); letter-spacing: -1px; margin-right: 10px; }
  .holder-last { font-size: 42px; color: var(--deep-green); }
  .holder-title {
    margin-top: 6px;
    font-size: 22px;
    font-weight: 400;
    color: var(--leaf-green);
  }

  .contact-list { position: absolute; left: 340px; top: 212px; list-style: none; }
  .contact-item {
    display: flex; align-items: center;
    height: 33px;
    font-size: 12px;
    color: var(--ink-blue);
  }
  .contact-icon { width: 28px; height: 26px; margin-right: 24px; }
  .contact-icon * { fill: none; stroke: var(--ink-blue); stroke-width: 2; }
  .contact-icon .solid { fill: var(--ink-blue); stroke: none; }

  .address {
    position: absolute; left: 0; right: 0; top: 374px;
    padding-left: 28px;
    text-align: center;
    font-size: 14px;
    letter-spacing: 0.3px;
    color: var(--ink-blue);
  }
</style>
</head>
<body>

<section class="card card-front">
  <div class="emblem-area" role="img" aria-label="Illustration of a green globe covered in trees and rivers, held by two open hands"></div>
  <h1 class="brand-name">VELMIRA HOTEL</h1>
  <p class="brand-name-zh" lang="zh-Hant">岚柏商旅</p>
</section>

<section class="card card-back">
  <svg class="frame-lines" viewBox="0 0 894 511" preserveAspectRatio="none" aria-hidden="true">
    <path d="M54 0 L33 474 L102 511"/>
    <path d="M0 41 L54 0"/>
    <path d="M717 0 L799 21 L809 464 L627 511"/>
    <path d="M802 0 L894 151"/>
    <path d="M832 0 L894 71"/>
    <path d="M0 276 L162 511"/>
    <path d="M0 316 L97 511"/>
    <path d="M894 231 L812 511"/>
    <path d="M894 371 L607 511"/>
  </svg>

  <div class="holder">
    <p class="holder-name"><span class="holder-first">Daniel</span><span class="holder-last">Hsu</span></p>
    <p class="holder-title">Manager</p>
  </div>

  <ul class="contact-list">
    <li class="contact-item">
      <svg class="contact-icon" viewBox="0 0 28 26" aria-hidden="true">
        <path class="solid" d="M17 2 l6 3 -3 5 -3 -1 c-2 3 -4 6 -5 9 l3 1 -2 6 -6 -2 c0 -8 4 -16 10 -21z"/>
      </svg>
      <span>55 712 308 941</span>
    </li>
    <li class="contact-item">
      <svg class="contact-icon" viewBox="0 0 28 26" aria-hidden="true">
        <rect x="2" y="5" width="24" height="16"/>
        <path d="M2 5 L14 15 L26 5"/>
      </svg>
      <span>velmira@hotel.tw</span>
    </li>
    <li class="contact-item">
      <svg class="contact-icon" viewBox="0 0 28 26" aria-hidden="true">
        <circle cx="14" cy="13" r="11"/>
        <ellipse cx="14" cy="13" rx="5" ry="11"/>
        <path d="M3 13 H25 M5 7 H23 M5 19 H23"/>
      </svg>
      <span>www.hotelvelmira.com</span>
    </li>
  </ul>

  <p class="address">42/3 , east linden avenue , hotel velmira</p>
</section>

</body>
</html>
```